movie poster for a bittersweet romantic drama

Hello everyone. Looking for a dynamic poster for feature film 'Mabel's Harbor' a romantic drama. It is a bittersweet love story so not rosey lovie dovie type.

300dpi

Please visit the link below for the poster image
https://www.filevault-example.net/s/k8p2r41xqz7mv5b/_Q7T4416.tif?dl=0

poster should have:
1. title of film : Mabel's Harbor
2. tagline of film:
Death knows no names
Love does not know race

3. A film by Lucinda P. Okwemba
4 Include the logo for 'Teruvo Films' attached below

poster size:
1. 8x10
2. thumnail
3. landscape with just film title
4. 27 by 41

Target Market(s)

15-55 men and mostly women

Industry/Entity Type

Film Production

Colors

Designer to choose colors to be used in the design.

Requirements
Must have
• Dynamic and vibrant
• it is a romantic drama so love on a serious note
Nice to have
• Play with romantic fonts but don't overdo it.
Should not have
• must not look like a romance novel

```html
<!DOCTYPE html>
<html lang="en">
<head>
<meta charset="utf-8">
<title>Mabel's Harbor — Title Poster</title>
<link href="https://fonts.googleapis.com/css2?family=Cinzel:wght@400;500&family=Yellowtail&display=swap" rel="stylesheet">
<style>
  :root {
    --paper: #ffffff;
    --title-red: #e8343a;
    --ink: #333333;
  }
  html, body {
    margin: 0;
    padding: 0;
    overflow: hidden;
    background: var(--paper);
  }
  .poster {
    position: relative;
    width: 1200px;
    height: 849px;
    background: var(--paper);
    overflow: hidden;
  }
  .title-main {
    position: absolute;
    left: 88px;
    top: 252px;
    margin: 0;
    font-family: "Cinzel", serif;
    font-weight: 400;
    font-size: 182px;
    line-height: 1;
    letter-spacing: 2px;
    color: var(--title-red);
    white-space: nowrap;
  }
  .title-script {
    position: absolute;
    left: 470px;
    top: 318px;
    margin: 0;
    font-family: "Yellowtail", cursive;
    font-weight: 400;
    font-size: 210px;
    line-height: 1;
    color: var(--ink);
    white-space: nowrap;
  }
  .tagline {
    position: absolute;
    left: 657px;
    top: 540px;
    margin: 0;
    font-family: "Cinzel", serif;
    font-size: 14.5px;
    line-height: 17px;
    letter-spacing: 0.3px;
    color: var(--title-red);
  }
  .credit {
    position: absolute;
    left: 659px;
    top: 602px;
    font-family: "Cinzel", serif;
    color: var(--ink);
  }
  .credit-label {
    display: block;
    font-size: 10.5px;
    letter-spacing: 0.5px;
    line-height: 12px;
  }
  .credit-name {
    display: block;
    font-size: 19px;
    letter-spacing: 0.6px;
    line-height: 22px;
  }
  .studio {
    position: absolute;
    left: 662px;
    top: 690px;
    display: flex;
    align-items: center;
    gap: 8px;
    font-family: "Cinzel", serif;
    font-weight: 500;
    font-size: 15px;
    letter-spacing: 0.6px;
    color: var(--ink);
  }
  .studio-mark {
    width: 12px;
    height: 12px;
    border-radius: 50%;
    background: var(--ink);
  }
</style>
</head>
<body>
  <main class="poster">
    <h1 class="title-main">MABEL’S</h1>
    <p class="title-script">Harbor</p>
    <p class="tagline">DEATH KNOWS NO NAMES<br>LOVE DOES NOT KNOW RACE</p>
    <div class="credit">
      <span class="credit-label">A FILM BY</span>
      <span class="credit-name">LUCINDA P. OKWEMBA</span>
    </div>
    <div class="studio">
      <span class="studio-mark"></span>
      <span class="studio-name">Teruvo Films</span>
    </div>
  </main>
</body>
</html>
```